Business Card Design Project

We need a business card designed for a new Luxury Custom Homebuilding company based in Arizona. We previous were called "Brellcrest Estates" but want to start using "Brellcrest Custom Homes" We want the message to communicate high end, luxury and cutting-edge. We like the blue, white and black color scheme.
Brellcrest Custom Homes
Marcus T. Pellingham
Chief Executive Officer
Office: 480-555-0142
Mobile: 480-555-0173
email: marcus@brellcrestcustom.com
web adress: www.BrellcrestCustom.com
Updates
We have made a change to our website address and email address based on recieving feedback from a nmber of individuals. The feedback was web address and email address was to long. Therefore we have made a change. The new web adress and email adress are the following.
www.BrellcrestCustom.com
marcus@brellcrestcustom.com
Also I decided against using in yellow. I like the colors blue,black, white and maybe gray.
Target Market(s)
Our target market is the wealthy individuals looking for a luxury high-end custom home.
Industry/Entity Type
Business
Look and feel
Each slider illustrates characteristics of the customer's brand and the style your logo design should communicate.

```html
<!DOCTYPE html>
<html lang="en">
<head>
<meta charset="utf-8">
<title>Brellcrest Custom Homes – Business Card</title>
<link rel="stylesheet" href="https://fonts.googleapis.com/css2?family=Oswald:wght@500;700&family=Roboto+Condensed:wght@400;700&display=swap">
<style>
  :root {
    --sky: #5f9bd6;
    --sky-soft: #8fbbe6;
    --ink: #000000;
    --paper: #ffffff;
    --stage: #e6e7ea;
    --name-blue: #5f9bd6;
  }
  * { box-sizing: border-box; margin: 0; padding: 0; }
  html, body { width: 1200px; height: 750px; overflow: hidden; }
  body {
    background: var(--stage);
    position: relative;
    font-family: "Roboto Condensed", "Arial Narrow", sans-serif;
  }
  .card {
    position: absolute;
    top: 215px;
    width: 525px;
    height: 300px;
    overflow: hidden;
    box-shadow: 0 6px 18px rgba(0,0,0,.25);
  }
  .card--front { left: 50px; background: var(--sky); }
  .card--back { left: 625px; background: var(--sky); }

  .card__shapes { position: absolute; inset: 0; width: 100%; height: 100%; }

  .brand {
    position: absolute;
    left: 58px;
    top: 50px;
    color: var(--paper);
    font-family: "Oswald", "Arial Narrow", sans-serif;
    font-weight: 700;
    line-height: 0.95;
    text-transform: uppercase;
  }
  .brand__mark {
    display: inline-block;
    width: 14px; height: 14px;
    background: var(--paper);
    border-radius: 50%;
    margin-right: 10px;
    vertical-align: 6px;
  }
  .brand__name { font-size: 44px; letter-spacing: -0.5px; }
  .brand__sub { display: block; font-size: 24px; margin-left: 24px; letter-spacing: 0.5px; }

  .address {
    position: absolute;
    left: 58px;
    top: 158px;
    color: var(--paper);
    font-size: 12.5px;
  }
  .contact-list {
    position: absolute;
    left: 70px;
    top: 185px;
    list-style: none;
    color: var(--paper);
    font-size: 13px;
  }
  .contact-list li { display: flex; align-items: center; height: 21px; }
  .address { display: flex; align-items: center; }
  .icon { width: 11px; height: 11px; margin-right: 7px; flex: none; }

  .holder {
    position: absolute;
    left: 38px;
    top: 30px;
    color: var(--paper);
  }
  .holder__name { font-family: "Oswald", "Arial Narrow", sans-serif; font-weight: 700; font-size: 21px; }
  .holder__title { font-size: 14px; margin-top: 2px; }

  .wordmark {
    position: absolute;
    left: 150px;
    top: 95px;
    color: var(--paper);
    font-family: "Oswald", "Arial Narrow", sans-serif;
    font-weight: 700;
    text-transform: uppercase;
    line-height: 0.95;
  }
  .wordmark__name { display: block; font-size: 62px; letter-spacing: -1px; }
  .wordmark__sub { display: block; font-size: 32px; margin-left: 120px; letter-spacing: 1px; }

  .web {
    position: absolute;
    left: 0; right: 0;
    bottom: 28px;
    text-align: center;
    color: var(--paper);
    font-weight: 700;
    font-size: 14px;
    letter-spacing: 6px;
  }
</style>
</head>
<body>

<section class="card card--front" aria-label="Business card front">
  <svg class="card__shapes" viewBox="0 0 525 300" preserveAspectRatio="none" aria-hidden="true">
    <path d="M40 0 H525 V185 C440 205 360 250 250 262 C170 270 90 262 40 252 Q20 180 40 0 Z" fill="var(--ink)"/>
    <path d="M40 0 C10 60 5 160 40 252" fill="none" stroke="var(--paper)" stroke-width="3"/>
    <path d="M52 0 C28 60 24 150 58 240" fill="none" stroke="var(--paper)" stroke-width="1.5"/>
    <path d="M0 255 C120 285 240 285 330 250 C400 222 460 195 525 188 V200 C460 210 400 238 330 268 C240 300 120 300 0 280 Z" fill="var(--paper)"/>
  </svg>

  <div class="brand">
    <span class="brand__name"><span class="brand__mark"></span>Brellcrest</span>
    <span class="brand__sub">Estates</span>
  </div>

  <p class="address">
    <svg class="icon" viewBox="0 0 12 12" aria-hidden="true"><circle cx="6" cy="6" r="6" fill="var(--sky)"/><circle cx="6" cy="5" r="2" fill="var(--ink)"/></svg>
    1480 S. Harlow Road, Suite 210, Mesa, AZ 85212
  </p>

  <ul class="contact-list">
    <li>
      <svg class="icon" viewBox="0 0 12 12" aria-hidden="true"><circle cx="6" cy="6" r="6" fill="var(--sky)"/><path d="M4 3 L5 3 L5.5 5 L4.8 5.6 Q5.6 7 6.6 7.4 L7.2 6.6 L9 7.2 L9 8.2 Q6 9 3.6 4.4 Z" fill="var(--ink)"/></svg>
      480-555-0142
    </li>
    <li>
      <svg class="icon" viewBox="0 0 12 12" aria-hidden="true"><rect x="3.5" y="1" width="5" height="10" rx="1" fill="var(--sky)"/><rect x="4.5" y="2.5" width="3" height="5" fill="var(--ink)"/></svg>
      480-555-0173
    </li>
    <li>
      <svg class="icon" viewBox="0 0 12 12" aria-hidden="true"><circle cx="6" cy="6" r="6" fill="var(--sky)"/><rect x="3" y="4" width="6" height="4.2" fill="var(--ink)"/><path d="M3 4 L6 6.4 L9 4" fill="none" stroke="var(--sky)" stroke-width=".8"/></svg>
      marcus@brellcrestcustom.com
    </li>
  </ul>
</section>

<section class="card card--back" aria-label="Business card back">
  <div class="holder">
    <p class="holder__name">Marcus T. Pellingham</p>
    <p class="holder__title">Chief Executive Office</p>
  </div>

  <div class="wordmark">
    <span class="wordmark__name">Brellcrest</span>
    <span class="wordmark__sub">Custom Homes</span>
  </div>

  <p class="web">www.BrellcrestCustom.com</p>
</section>

</body>
</html>
```